Real Estate Development Company Stationary

We need our company, business card, letterhead, pocket folder and envelope designed.

We are a new real estate development company. We focus on data centre, commercial and real estate development.

Please see attached for our logo. Since it's a new logo, you still can make minor adjust if you like it makes senses

The client has sent me a business card he really likes. Please see file 3.

Target Market(s)

Real Estate Investors
Large corporations
Home buyers

Industry/Entity Type

Real Estate

```html
<!DOCTYPE html>
<html lang="en">
<head>
<meta charset="utf-8">
<title>Kestrel Development Inc. — Stationery</title>
<link rel="stylesheet" href="https://fonts.googleapis.com/css2?family=Source+Sans+3:ital,wght@0,400;0,600;1,400&display=swap">
<style>
  :root {
    --backdrop: #cfcfcf;
    --paper: #ffffff;
    --brand-green: #5fb83a;
    --brand-blue: #1f5aa6;
    --ink-blue: #2b5f9e;
    --ink-muted: #6b7f99;
    --edge: rgba(0,0,0,0.18);
  }
  * { box-sizing: border-box; margin: 0; padding: 0; }
  html, body {
    width: 1200px; height: 1000px; overflow: hidden;
    background: var(--backdrop);
    font-family: "Source Sans 3", sans-serif;
  }
  .stationery-set { position: relative; width: 1200px; height: 1000px; }

  .sheet {
    position: absolute; background: var(--paper); overflow: hidden;
    box-shadow: 0 2px 0 #e9e9e9, 0 4px 0 #dedede, 0 6px 14px var(--edge);
  }

  .wordmark {
    position: absolute; display: flex; align-items: center; gap: 6px;
    color: var(--brand-green); font-weight: 600; white-space: nowrap; line-height: 1;
  }
  .wordmark .mark-dot {
    border-radius: 50%; background: var(--brand-blue); flex: none;
  }

  .contact {
    position: absolute; text-align: right; color: var(--ink-blue);
    line-height: 1.35; white-space: nowrap;
  }

  /* Letterhead */
  .letterhead { left: 70px; top: 110px; width: 480px; height: 620px; }
  .letterhead .wordmark { left: 32px; top: 32px; font-size: 15px; }
  .letterhead .mark-dot { width: 12px; height: 12px; }
  .letterhead .contact { right: 34px; bottom: 28px; font-size: 8px; }

  /* Business card */
  .business-card { left: 640px; top: 150px; width: 330px; height: 190px; }
  .business-card .wordmark { left: 22px; top: 42px; font-size: 11px; }
  .business-card .mark-dot { width: 9px; height: 9px; }
  .card-holder { position: absolute; right: 26px; top: 34px; text-align: right; }
  .card-holder .name { color: var(--ink-blue); font-size: 14px; font-weight: 600; }
  .card-holder .role { color: var(--ink-muted); font-size: 10px; font-style: italic; }
  .business-card .contact { right: 26px; bottom: 24px; font-size: 7.5px; }

  /* Envelope */
  .envelope { left: 620px; top: 420px; width: 510px; height: 220px; }
  .envelope .wordmark { left: 36px; top: 74px; font-size: 17px; }
  .envelope .mark-dot { width: 13px; height: 13px; }
  .envelope .contact { right: 28px; bottom: 20px; font-size: 8px; }
</style>
</head>
<body>
<main class="stationery-set">

  <section class="sheet letterhead" aria-label="Letterhead">
    <div class="wordmark"><span class="mark-dot"></span>Kestrel Development Inc.</div>
    <p class="contact">T. 555 014 2290 C. 555 017 3342<br>www.kestreldev.example</p>
  </section>

  <section class="sheet business-card" aria-label="Business card">
    <div class="wordmark"><span class="mark-dot"></span>Kestrel Development Inc.</div>
    <div class="card-holder">
      <p class="name">Dana Okafor</p>
      <p class="role">Project Manager</p>
    </div>
    <p class="contact">T. 555 014 2290 C. 555 017 3342<br>dana@kestreldev.example<br>www.kestreldev.example</p>
  </section>

  <section class="sheet envelope" aria-label="Envelope">
    <div class="wordmark"><span class="mark-dot"></span>Kestrel Development Inc.</div>
    <p class="contact">T. 555 014 2290 C. 555 017 3342<br>www.kestreldev.example</p>
  </section>

</main>
</body>
</html>
```